Business Card Design for BrightwaveOutreach.com

--I need a business card design for my company BrightwaveOutreach.com

I have attached my logo...I want the brightwave outreach logo on the front of the business card, and then I want The Brightwave Chief on the back of it with my information.

I would like to see a light colored background as well as a dark colored background

FRONT:
BRIGHTWAVE OUTREACH LOGO
482 N. Elmwood
3rd Floor
San Diego CA 92101
www.BrightwaveOutreach.com

Advanced Website & App Development
Websites, Apps, Online Voucher Systems

Leading Edge Marketing Services
SMS, VB, SMM, SEM,

BACK:
BRIGHTWAVE CHIEF LOGO
Dorian Pelley
The Brightwave Chief
Call Or Text: 619-555-0148
Dorian@BrightwaveChief.com
www.BrightwaveChief.com

Target Market(s)

small business owners

Industry/Entity Type

Business Consultant

Contact Information for Business Card

FRONT:
BRIGHTWAVE OUTREACH LOGO
482 N. Elmwood
3rd Floor
San Diego CA 92101
www.BrightwaveOutreach.com

SMS, VB, SMM, SEM,

BACK:
BRIGHTWAVE CHIEF LOGO
Dorian Pelley
The Brightwave Chief
Dorian@BrightwaveChief.com
www.BrightwaveChief.com

Requirements
Must have
• add this quote on it somewhere, anywhere,preferrably on back
• "The Fastest Way To Success Is To Take Action”
• — Dorian Pelley, Brightwave Chief
Nice to have
• open
Should not have
• red

```html
<!DOCTYPE html>
<html lang="en">
<head>
<meta charset="utf-8">
<title>Brightwave Outreach – Business Cards</title>
<link href="https://fonts.googleapis.com/css2?family=Lato:wght@400;700&display=swap" rel="stylesheet">
<style>
  :root {
    --stage: #2b2b2b;
    --blue-light: #2a8fd0;
    --blue-mid: #1a73b3;
    --blue-deep: #0f5a92;
    --navy: #0d4f8b;
    --ink: #1c1c1c;
    --grey-band: #4a4a4a;
    --paper: #f7f7f7;
    --white: #ffffff;
    --rule-light: rgba(255,255,255,.7);
  }
  * { margin: 0; padding: 0; box-sizing: border-box; }
  html, body { width: 1200px; height: 873px; overflow: hidden; }
  body {
    background: var(--stage);
    font-family: "Lato", sans-serif;
    position: relative;
  }
  .card {
    position: absolute;
    width: 560px;
    height: 320px;
    overflow: hidden;
    box-shadow: 0 12px 30px rgba(0,0,0,.45);
  }

  /* Front card */
  .card--front {
    left: 70px; top: 100px;
    background: linear-gradient(160deg, var(--blue-light) 0%, var(--blue-mid) 55%, var(--blue-deep) 100%);
    color: var(--white);
  }
  .front-name {
    position: absolute;
    left: 40px; top: 44px;
    font-weight: 700;
    letter-spacing: 4px;
    line-height: 1.1;
  }
  .front-name .primary { display: block; font-size: 42px; }
  .front-name .secondary { display: block; font-size: 17px; letter-spacing: 10px; margin-top: 4px; }
  .front-services {
    position: absolute;
    left: 40px; right: 40px; top: 166px;
    display: flex;
    align-items: stretch;
    font-size: 12.5px;
    line-height: 1.7;
    white-space: nowrap;
  }
  .service-col--left { padding-right: 22px; }
  .service-col--right { padding-left: 22px; }
  .front-divider {
    width: 1px;
    background: var(--rule-light);
  }
  .front-address {
    position: absolute;
    left: 40px; right: 40px; bottom: 64px;
    font-size: 14px; font-weight: 700;
    text-align: center;
  }
  .front-web {
    position: absolute;
    left: 40px; right: 40px; bottom: 30px;
    display: flex; align-items: center; gap: 14px;
    font-size: 14px; font-weight: 700;
  }
  .front-web .rule { flex: 1; height: 1px; background: var(--rule-light); }

  /* Back card */
  .card--back {
    left: 570px; top: 450px;
    background: var(--paper);
    color: var(--ink);
  }
  .back-name {
    position: absolute;
    right: 40px; top: 34px;
    text-align: right;
    font-weight: 700;
    color: var(--navy);
    letter-spacing: 3px;
    line-height: 1.1;
  }
  .back-name .primary { display: block; font-size: 36px; }
  .back-name .secondary { display: block; font-size: 16px; letter-spacing: 10px; margin-top: 2px; }
  .person {
    position: absolute;
    left: 44px; top: 138px;
    text-align: right;
    width: 200px;
  }
  .person-name { font-size: 20px; font-weight: 700; color: var(--navy); }
  .person-title { font-size: 15px; margin-top: 2px; }
  .back-divider {
    position: absolute;
    left: 262px; top: 108px;
    width: 3px; height: 104px;
    background: linear-gradient(180deg, rgba(13,79,139,0) 0%, var(--navy) 50%, rgba(13,79,139,0) 100%);
  }
  .contacts {
    position: absolute;
    left: 284px; top: 112px;
    list-style: none;
    font-size: 15px;
  }
  .contacts li { display: flex; align-items: center; gap: 10px; height: 30px; }
  .contacts svg { width: 16px; height: 16px; fill: var(--navy); flex: none; }
  .band-blue {
    position: absolute;
    right: 0; bottom: 58px;
    width: 240px; height: 34px;
    background: var(--navy);
    border-top-left-radius: 50px 34px;
  }
  .band-base {
    position: absolute; left: 0; right: 0; bottom: 0; height: 60px;
    background: var(--paper);
  }
  .band-bottom {
    position: absolute; left: 0; right: 0; bottom: 0; height: 10px;
    background: var(--grey-band);
  }
  .tagline {
    position: absolute;
    left: 36px; bottom: 24px;
    font-size: 17px; font-weight: 700;
    color: var(--navy);
  }
</style>
</head>
<body>

<section class="card card--front" aria-label="Business card front">
  <div class="front-name">
    <span class="primary">BRIGHTWAVE</span>
    <span class="secondary">OUTREACH</span>
  </div>
  <div class="front-services">
    <div class="service-col service-col--left">
      Advanced Website &amp; App Development<br>
      Websites, Apps, Online Voucher Systems
    </div>
    <div class="front-divider"></div>
    <div class="service-col service-col--right">
      Leading Edge Marketing Services<br>
      SMS, VB, SMM, SEM,
    </div>
  </div>
  <p class="front-address">482 N. Elmwood, 3rd Floor, San Diego CA 92101</p>
  <div class="front-web">
    <span class="rule"></span>
    <span>www.BrightwaveOutreach.com</span>
    <span class="rule"></span>
  </div>
</section>

<section class="card card--back" aria-label="Business card back">
  <div class="back-name">
    <span class="primary">BRIGHTWAVE</span>
    <span class="secondary">CHIEF</span>
  </div>

  <div class="person">
    <p class="person-name">Dorian Pelley</p>
    <p class="person-title">The Brightwave Chief</p>
  </div>
  <div class="back-divider"></div>

  <ul class="contacts">
    <li>
      <svg viewBox="0 0 24 24" aria-hidden="true"><path d="M6.6 10.8a15.1 15.1 0 0 0 6.6 6.6l2.2-2.2a1 1 0 0 1 1-.25 11.4 11.4 0 0 0 3.6.57 1 1 0 0 1 1 1V20a1 1 0 0 1-1 1A17 17 0 0 1 3 4a1 1 0 0 1 1-1h3.5a1 1 0 0 1 1 1c0 1.25.2 2.45.57 3.570a1 1 0 0 1-.25 1z"/></svg>
      619-555-0148
    </li>
    <li>
      <svg viewBox="0 0 24 24" aria-hidden="true"><path d="M2 5h20v14H2zm2 2v.4l8 5 8-5V7zm0 2.8V17h16V9.8l-8 5z"/></svg>
      Dorian@BrightwaveChief.com
    </li>
    <li>
      <svg viewBox="0 0 24 24" aria-hidden="true"><path d="M10.6 13.4a1 1 0 0 1 0-1.4l3.5-3.5a1 1 0 1 1 1.4 1.4L12 13.4a1 1 0 0 1-1.4 0zM8 18.5a3.5 3.5 0 0 1-2.5-6l2.1-2.1 1.4 1.4-2.1 2.1a1.5 1.5 0 0 0 2.1 2.1l2.1-2.1 1.4 1.4-2.1 2.1A3.5 3.5 0 0 1 8 18.5zm8.4-4.9L15 12.2l2.1-2.1a1.5 1.5 0 0 0-2.1-2.1l-2.1 2.1-1.4-1.4 2.1-2.1a3.5 3.5 0 0 1 5 5z"/></svg>
      www.BrightwaveChief.com
    </li>
  </ul>

  <div class="band-blue"></div>
  <div class="band-base"></div>
  <div class="band-bottom"></div>
  <p class="tagline">The Fastest Way To Success Is To Take Action</p>
</section>

</body>
</html>
```